Watch repair & restoration postcard design

Marlow Heirloom Jewelry (555-471-3286) 27310 W. Pell Rd. Suite #D
Goal
looking to increase Watch repair and restoration primarily on higher end watches Vantor, Kessmark, Durel. etc etc
Expert mechanical watch servicing including automatics
Parts replacement crystal, dial, hands etc. etc.
Complete restoration
Fast turnaround
Industry/Entity Type
Jewelry

```html
<!DOCTYPE html>
<html lang="en">
<head>
<meta charset="UTF-8">
<title>Marlow Heirloom Jewelry – Watch Repair Postcard</title>
<link href="https://fonts.googleapis.com/css2?family=Libre+Baskerville&family=Roboto+Condensed:wght@400;700&display=swap" rel="stylesheet">
<style>
  :root {
    --bg: #2b2b2d;
    --card: #ffffff;
    --magenta: #9c1f5c;
    --magenta-soft: #e9c3d6;
    --ink: #3a3a3a;
    --gold: #f2c230;
    --rule: #6d6d6d;
    --steel-1: #d9d4cc;
    --steel-2: #9a8f80;
    --bronze: #b89a6a;
  }
  * { box-sizing: border-box; margin: 0; padding: 0; }
  html, body { width: 900px; height: 1200px; overflow: hidden; }
  body { background: var(--bg); font-family: "Roboto Condensed", Arial, sans-serif; position: relative; }

  .postcard { position: absolute; left: 30px; width: 840px; height: 560px; background: var(--card); overflow: hidden; box-shadow: 0 6px 18px rgba(0,0,0,.4); }
  .postcard--front { top: 25px; }
  .postcard--back { top: 615px; }

  /* Front */
  .front-art { position: absolute; inset: 0; }
  .brand { position: absolute; left: 60px; top: 345px; }
  .brand__name { font-family: "Libre Baskerville", Georgia, serif; font-size: 36px; color: var(--ink); letter-spacing: .5px; }
  .brand__phone { font-weight: 700; font-size: 22px; color: var(--ink); margin: 6px 0 0 110px; }
  .brand__address { font-weight: 700; font-size: 24px; color: var(--ink); margin-top: 6px; margin-left: 40px; }
  .movement-photo { position: absolute; left: 540px; top: 300px; width: 240px; height: 240px; border-radius: 50%;
    background: radial-gradient(circle at 45% 40%, #f4f1ea 0%, #c9c3b8 35%, #8c867c 65%, #c7b27f 80%, #e9dcb5 100%); }

  /* Back */
  .back-accent { position: absolute; inset: 0; }
  .goal { position: absolute; left: 40px; top: 38px; width: 390px; }
  .goal__tab { display: inline-block; background: var(--gold); color: var(--ink); font-weight: 700; font-size: 22px;
    padding: 4px 34px 4px 14px; border-radius: 0 16px 16px 0; }
  .goal__list { list-style: none; margin-top: 8px; color: var(--magenta); font-weight: 700; font-size: 22px; line-height: 1.22; }
  .watch-photo { position: absolute; left: 40px; top: 385px; width: 360px; height: 150px; border: 5px solid var(--magenta); border-radius: 22px;
    background: linear-gradient(135deg, #ece9e2 0%, #ffffff 40%, #d8cfbd 70%, #b9a574 100%); }
  .divider { position: absolute; left: 488px; top: 100px; width: 2px; height: 360px; background: var(--rule); }
  .stamp { position: absolute; left: 660px; top: 70px; width: 100px; height: 100px; border: 2px solid var(--rule); }
  .address-line { position: absolute; left: 540px; width: 240px; height: 2px; background: var(--rule); }
</style>
</head>
<body>

<section class="postcard postcard--front">
  <svg class="front-art" width="840" height="560" viewBox="0 0 840 560">
    <defs>
      <linearGradient id="movementTone" x1="0" y1="0" x2="1" y2="1">
        <stop offset="0" stop-color="#cdbfa6"/>
        <stop offset=".45" stop-color="#e7e2d9"/>
        <stop offset=".75" stop-color="#a39a8c"/>
        <stop offset="1" stop-color="#c9b487"/>
      </linearGradient>
    </defs>
    <rect width="840" height="330" fill="url(#movementTone)" role="img" aria-label="Close-up photograph of a mechanical watch movement with gears"/>
    <path d="M0 300 C 200 250, 380 340, 560 300 S 780 230, 840 250 L 840 560 L 0 560 Z" fill="#ffffff"/>
    <path d="M0 318 C 200 268, 380 358, 560 318 S 780 248, 840 268" fill="none" stroke="var(--magenta)" stroke-width="6"/>
  </svg>
  <div class="movement-photo" role="img" aria-label="Photograph of an open-back automatic watch movement"></div>
  <div class="brand">
    <p class="brand__name">Marlow Heirloom Jewelry</p>
    <p class="brand__phone">(555) 471-3286</p>
    <p class="brand__address">27310 W. Pell Rd. Suite #D</p>
  </div>
</section>

<section class="postcard postcard--back">
  <svg class="back-accent" width="840" height="560" viewBox="0 0 840 560">
    <path d="M0 0 L 220 0 C 140 20, 60 50, 0 110 Z" fill="var(--magenta-soft)"/>
    <path d="M0 120 C 60 60, 140 26, 230 0" fill="none" stroke="var(--magenta)" stroke-width="3"/>
  </svg>
  <div class="goal">
    <h2 class="goal__tab">Our Goal</h2>
    <ul class="goal__list">
      <li>looking to increase Watch repair and<br>restoration primarily on higher end watches<br>Vantor, Kessmark, Durel, etc.</li>
      <li>Expert mechanical watch<br>servicing including automatics</li>
      <li>Parts replacement crystal, dial,<br>hands etc. etc.</li>
      <li>Complete restoration</li>
      <li>Fast turnaround</li>
    </ul>
  </div>
  <div class="watch-photo" role="img" aria-label="Photograph of a gold dress watch face"></div>
  <div class="divider"></div>
  <div class="stamp"></div>
  <div class="address-line" style="top:250px"></div>
  <div class="address-line" style="top:300px"></div>
  <div class="address-line" style="top:350px"></div>
  <div class="address-line" style="top:400px"></div>
</section>

</body>
</html>
```